Land Buying Company Needs Letterhead for Direct Mail Marketing to Land Owners

We are looking for a professional letterhead that we will be including in our direct mail marketing. We will be sending this to land owners who may be interested in selling or purchasing land.

The letterhead needs to be editable. Headers and footers would look nice, but we are open. We would want it to include our address, website, phone, and email info. For right now the address to use for design purposes would the following:

Address: 415 Bramwell Avenue #600
Dallas, TX 75219
Website - www.quillridgeacres.example
Email - info@quillridgeacres.example
Phone - 866-402-ACRE

I have attached our logo zip file that we just had done on Pixel Guild. Let me know what questions you have, and thank you.

```html
<!DOCTYPE html>
<html lang="en">
<head>
<meta charset="utf-8">
<title>Quillridge Acres Letterhead</title>
<link href="https://fonts.googleapis.com/css2?family=Montserrat:wght@400;500;700&family=Roboto:wght@400&display=swap" rel="stylesheet">
<style>
  :root {
    --green-dark: #3f5a1f;
    --green-light: #8cc63e;
    --text: #7a7a7a;
    --text-dark: #333333;
    --paper: #ffffff;
    --backdrop: #ececec;
  }
  * { box-sizing: border-box; margin: 0; padding: 0; }
  html, body { width: 1110px; height: 1200px; overflow: hidden; }
  body { background: var(--backdrop); font-family: "Montserrat", sans-serif; }
  .letterhead {
    position: absolute; left: 126px; top: 0;
    width: 857px; height: 1200px;
    background: var(--paper); overflow: hidden;
  }
  .brand {
    position: absolute; top: 44px; left: 0; width: 100%;
    display: flex; justify-content: center; align-items: center; gap: 14px;
  }
  .brand-dot { width: 54px; height: 54px; border-radius: 50%; background: var(--green-dark); }
  .brand-name {
    font-weight: 700; font-size: 30px; letter-spacing: 1px;
    color: var(--green-dark); text-transform: uppercase;
  }
  .recipient { position: absolute; left: 88px; top: 268px; font-size: 11px; color: var(--text); line-height: 19px; }
  .recipient .label { font-size: 15px; color: var(--text-dark); letter-spacing: 2px; margin-bottom: 4px; }
  .recipient .name { font-size: 13px; color: var(--green-light); }
  .date { position: absolute; right: 85px; top: 272px; font-size: 12px; color: var(--text); }
  .body-copy {
    position: absolute; left: 88px; top: 424px; width: 685px;
    font-size: 12px; line-height: 15.4px; color: var(--text); text-align: justify;
  }
  .body-copy p { margin-bottom: 15px; }
  .sign-off { position: absolute; left: 88px; top: 852px; }
  .signature { width: 150px; height: 28px; background: linear-gradient(90deg, #d9d9d9, #eeeeee); border-radius: 3px; margin-bottom: 14px; }
  .signer-name { font-size: 14px; color: var(--text-dark); }
  .signer-role { font-size: 11px; color: var(--text); margin-top: 2px; }
  .footer { position: absolute; left: 0; bottom: 0; width: 857px; height: 110px; }
  .footer svg.waves { position: absolute; left: 0; top: 0; }
  .footer-info {
    position: absolute; left: 0; width: 100%; text-align: center;
    font-family: "Roboto", sans-serif; color: #ffffff; font-size: 16px;
  }
  .footer-address { top: 47px; }
  .footer-contacts { top: 74px; display: flex; justify-content: center; gap: 22px; }
  .contact { display: flex; align-items: center; gap: 8px; }
  .contact svg { width: 12px; height: 12px; fill: #ffffff; }
</style>
</head>
<body>
  <main class="letterhead">
    <header class="brand">
      <span class="brand-dot"></span>
      <span class="brand-name">Quillridge Acres</span>
    </header>

    <section class="recipient">
      <div class="label">TO</div>
      <div class="name">Nora Lindqvist</div>
      <div>Human Resources</div>
      <div>Brightpath Inc.</div>
      <div>2207-B Halvern Road, Easton</div>
      <div>K42 USA</div>
    </section>
    <div class="date">Friday, 01/01/2018</div>

    <article class="body-copy">
      <p>Lorem ipsum dolor sit amet, consectetuer adipiscing elit, sed diam nonummy nibh euismod tincidunt ut laoreet dolore magna aliquam erat volutpat. Ut wisi enim ad minim veniam, quis nostrud exerci tationmcorper suscipit lobortis nisl ut aliquip ex ea commodo consequat. Duis autem vel eum iriure dolor in hendrerit in vulputate velit esse molestie consequat, vel illum dolore eu feugiat nulla facilisis at vero eros et accumsan et iusto odio dignissim qui blandit praesent luptatum zzril delenit augue duis dolore te feugait nulla facilisi.</p>
      <p>Nam liber tempor cum soluta nobis eleifend option congue nihil imprdiet doming id quod mazim placerat facer possim assum. Typi non habent claritatem insitam;</p>
      <p>Est usus legentis in iis qui facit eorum claritatem.</p>
      <p>Investigationes demonstraverunt lectores legere me lius quod ii legunt saepius. Claritas est etiam processus dynamicus, qui sequitur mutationem consuetudium lectorum. Mirum est notare quam littera gothica, quam nunc putamus parum claram, anteposuerit litterarum formas humanitatis per seacula quarta decima et quinta decima. Eodem modo typi, qui nunc nobis videntur parum clari, fiant sollemnes in futurum.</p>
      <p>consectetuer adipiscing elit, sed diam nonummy nibh euismod tincidunt ut laoreet dolore magna aliquam erat volutpat. Ut wisi enim ad minim veniam, quis nostrud exerci tation ullamcorper suscipit lobortis nisl ut aliquip ex ea commodo consequat. Duis autem vel eum iriure dolor in hendrerit in vulputate velit esse molestie consequat, vel illum dolore eu feugiat nulla facilisis at vero eros et accumsan et iusto odio dignissim qui blandit praesent luptatum zzril delenit augue duis dolore te feugait nulla facilisi.</p>
      <p>Nam liber tempor cum soluta nobis eleifend option congue nihil imperdiet .</p>
    </article>

    <section class="sign-off">
      <div class="signature" role="img" aria-label="Handwritten signature of Elliot Marsh"></div>
      <div class="signer-name">Elliot Marsh</div>
      <div class="signer-role">Managing Director</div>
    </section>

    <footer class="footer">
      <svg class="waves" width="857" height="110" viewBox="0 0 857 110">
        <path d="M0 24 C250 -2 560 -6 857 30 L857 36 C560 8 250 12 0 32 Z" fill="var(--green-light)"/>
        <path d="M0 30 C260 10 520 6 857 40 L857 110 L0 110 Z" fill="var(--green-dark)"/>
        <path d="M0 36 C240 18 480 16 700 30 C480 22 240 26 0 42 Z" fill="#ffffff"/>
      </svg>
      <div class="footer-info footer-address">415 Bramwell Avenue #600, Dallas, TX 75219</div>
      <div class="footer-info footer-contacts">
        <span class="contact">
          <svg viewBox="0 0 24 24"><path d="M6.6 10.8a15 15 0 0 0 6.6 6.6l2.2-2.2a1 1 0 0 1 1-.25 11.4 11.4 0 0 0 3.6.57 1 1 0 0 1 1 1V20a1 1 0 0 1-1 1A17 17 0 0 1 3 4a1 1 0 0 1 1-1h3.5a1 1 0 0 1 1 1c0 1.25.2 2.45.57 3.57a1 1 0 0 1-.25 1z"/></svg>
          866-402-ACRE
        </span>
        <span class="contact">
          <svg viewBox="0 0 24 24"><path d="M2 5h20v14H2z M2 5l10 8 10-8" fill="none" stroke="#fff" stroke-width="2.5"/></svg>
          info@quillridgeacres.example
        </span>
        <span class="contact">
          <svg viewBox="0 0 24 24"><circle cx="12" cy="12" r="10" fill="none" stroke="#fff" stroke-width="2.5"/><path d="M2 12h20M12 2c3 3 3 17 0 20M12 2c-3 3-3 17 0 20" fill="none" stroke="#fff" stroke-width="2"/></svg>
          www.quillridgeacres.example
        </span>
      </div>
    </footer>
  </main>
</body>
</html>
```